wine label

Label for wine, in black and silver, format to be in PDF ,EPS, PSD Label to be split main label to have Name: Morbray Ash family crest, dry grown, and Clare Valley
other section to have the type of wine ie: Grenache and year of harvest.
Some ideas we had our enclosed

```html
<!DOCTYPE html>
<html lang="en">
<head>
<meta charset="utf-8">
<title>Morbray Ash – Wine Labels</title>
<link rel="stylesheet" href="https://fonts.googleapis.com/css2?family=Cinzel:wght@700&family=Libre+Baskerville:wght@400;700&display=swap">
<style>
  :root {
    --page: #ffffff;
    --label: #050505;
    --label-edge: #9a9a9a;
    --silver: #d9d9d9;
    --silver-soft: #bdbdbd;
    --silver-deep: #6e6e6e;
    --ink-light: #ffffff;
  }
  html, body {
    margin: 0;
    padding: 0;
    width: 1200px;
    height: 960px;
    overflow: hidden;
    background: var(--page);
  }
  .canvas {
    position: relative;
    width: 1200px;
    height: 960px;
    background: var(--page);
  }
  .neck-label {
    position: absolute;
    left: 484px;
    top: 46px;
    width: 232px;
    height: 275px;
  }
  .main-label {
    position: absolute;
    left: 369px;
    top: 334px;
    width: 462px;
    height: 528px;
  }
  .variety-tab {
    position: absolute;
    left: 407px;
    top: 872px;
    width: 386px;
    height: 44px;
  }
  .serif {
    font-family: "Libre Baskerville", Georgia, serif;
  }
  .display {
    font-family: "Cinzel", "Times New Roman", serif;
    font-weight: 700;
  }
</style>
</head>
<body>
<main class="canvas">

  <!-- Neck label: variety and vintage -->
  <svg class="neck-label" viewBox="0 0 232 275" xmlns="http://www.w3.org/2000/svg">
    <defs>
      <radialGradient id="grapeTone" cx="50%" cy="45%" r="55%">
        <stop offset="0%" stop-color="#e6e6e6"/>
        <stop offset="100%" stop-color="#7a7a7a"/>
      </radialGradient>
    </defs>
    <rect x="1" y="1" width="230" height="273" rx="12" fill="var(--label)" stroke="var(--label-edge)" stroke-width="1.5"/>
    <text class="serif" x="116" y="58" text-anchor="middle" font-size="29" fill="var(--ink-light)">Grenache</text>
    <ellipse role="img" aria-label="Silver grape bunch illustration" cx="116" cy="145" rx="44" ry="62" fill="url(#grapeTone)"/>
    <text class="serif" x="116" y="250" text-anchor="middle" font-size="25" letter-spacing="2" fill="var(--ink-light)">2014</text>
  </svg>

  <!-- Main label: name, crest, growing method, region -->
  <svg class="main-label" viewBox="0 0 462 528" xmlns="http://www.w3.org/2000/svg">
    <defs>
      <radialGradient id="crestTone" cx="50%" cy="45%" r="55%">
        <stop offset="0%" stop-color="#dcdcdc"/>
        <stop offset="100%" stop-color="#5a5a5a"/>
      </radialGradient>
      <radialGradient id="flourishTone" cx="50%" cy="50%" r="50%">
        <stop offset="0%" stop-color="#3a3a3a"/>
        <stop offset="100%" stop-color="#050505"/>
      </radialGradient>
      <path id="nameArc" d="M 70 200 A 240 240 0 0 1 392 200"/>
    </defs>
    <rect x="1" y="1" width="460" height="526" rx="22" fill="var(--label)" stroke="var(--label-edge)" stroke-width="1.5"/>

    <ellipse role="img" aria-label="Faint silver flourish ornament, left" cx="70" cy="360" rx="62" ry="70" fill="url(#flourishTone)"/>
    <ellipse role="img" aria-label="Faint silver flourish ornament, right" cx="392" cy="360" rx="62" ry="70" fill="url(#flourishTone)"/>

    <text class="display" font-size="42" fill="var(--silver)" letter-spacing="1">
      <textPath href="#nameArc" startOffset="50%" text-anchor="middle">MORBRAY ASH</textPath>
    </text>

    <circle role="img" aria-label="Family crest in silver" cx="231" cy="255" r="90" fill="url(#crestTone)"/>

    <line x1="100" y1="381" x2="140" y2="381" stroke="var(--silver-soft)" stroke-width="1.2"/>
    <text class="serif" x="231" y="387" text-anchor="middle" font-size="17" letter-spacing="2" fill="var(--silver-soft)">DRY GROWN</text>
    <line x1="322" y1="381" x2="362" y2="381" stroke="var(--silver-soft)" stroke-width="1.2"/>

    <text class="serif" x="231" y="448" text-anchor="middle" font-size="38" fill="var(--silver)">Clare Valley</text>
  </svg>

  <!-- Variety strip below main label -->
  <svg class="variety-tab" viewBox="0 0 386 44" xmlns="http://www.w3.org/2000/svg">
    <rect x="1" y="1" width="384" height="42" rx="21" fill="var(--label)" stroke="var(--label-edge)" stroke-width="1.5"/>
    <text class="serif" x="193" y="29" text-anchor="middle" font-size="20" font-weight="700" fill="var(--ink-light)">Shiraz/Grenache 2013</text>
  </svg>

</main>
</body>
</html>
```